Harrowden Metal recycling, a business card/logo for our industrial family metal recycling company

A new business card design/logo for our long established family metal recycling company.
I have a logo for our property company which was designed a few months ago on pixel forge which I would like to be very close to this design but have a more industrial feel to it and in a darker blue colour, please see attachments.

Target Market(s)

industries that produce metal waste for recycling, construction sites, engineering companies, manufactures, builders, plumbers, electricians, general house holders.

Industry/Entity Type

Recycling

Contact Information for Business Card

owner/director...Martin harrowden
e-mail....info@harrowdenscrapworks.co.uk
web address.....harrowdenscrapworks.co.uk

Font styles to use
Serif
Sans Serif

Colors
0255a3
ffffff

Requirements
Must have
• -dark blue business card on front.
-white on the back, see contact details, e-mail address for metal company.
-to have an industrial feel to it.
-harrowden logo as business card attached but (harrowden metal recycling)
please remove the little roof/arrow above harrowden as this was relevant to property company.
Nice to have
• please see our website harrowdenscrapworks.co.uk with all details
being correct however I would like to refresh the logo to more like the harrowden property investment business card logo attached.
Should not have
• should not contain details from property investments card as this design is for the metal recycling company.

```html
<!DOCTYPE html>
<html lang="en">
<head>
<meta charset="utf-8">
<title>Harrowden Metal Recycling – Business Card</title>
<link rel="stylesheet" href="https://fonts.googleapis.com/css2?family=Poppins:ital,wght@0,400;0,600;0,800;1,700&family=Oswald:wght@500;700&display=swap">
<style>
  :root {
    --page-bg: #1d1f24;
    --brand-blue: #0255a3;
    --deep-blue: #1b2f8f;
    --navy: #1f2a6b;
    --bright-blue: #2a7be0;
    --white: #ffffff;
    --accent-red: #e0201b;
    --silver-dark: #9aa0a8;
    --silver-light: #f2f3f5;
  }
  * { box-sizing: border-box; margin: 0; padding: 0; }
  html, body { width: 1200px; height: 900px; overflow: hidden; }
  body {
    background: var(--page-bg);
    font-family: "Poppins", sans-serif;
    display: flex;
    flex-direction: column;
    align-items: center;
    justify-content: center;
    gap: 20px;
  }
  .card {
    position: relative;
    width: 735px;
    height: 420px;
    overflow: hidden;
    box-shadow: 0 10px 30px rgba(0,0,0,.5);
  }

  /* Front */
  .card--front {
    background:
      radial-gradient(ellipse 60% 40% at 25% 20%, rgba(90,170,255,.45), transparent 70%),
      radial-gradient(ellipse 50% 40% at 85% 85%, rgba(80,160,255,.35), transparent 70%),
      repeating-linear-gradient(-8deg, rgba(255,255,255,.035) 0 1px, transparent 1px 4px),
      linear-gradient(135deg, var(--brand-blue), var(--deep-blue) 55%, #2b2f8a);
    color: var(--white);
    display: flex;
    flex-direction: column;
    align-items: center;
    justify-content: center;
  }
  .brand-name {
    font-weight: 800;
    text-transform: uppercase;
    line-height: 1;
    text-align: center;
  }
  .card--front .brand-name { font-size: 58px; letter-spacing: 1px; }
  .card--front .brand-name span { display: block; }
  .card--front .brand-name .brand-sub { font-size: 38px; letter-spacing: 10px; margin-top: 6px; }
  .tagline {
    margin-top: 12px;
    padding-top: 8px;
    border-top: 1px solid rgba(255,255,255,.7);
    font-size: 12px;
    letter-spacing: 3px;
    text-transform: uppercase;
  }
  .front-web {
    position: absolute;
    bottom: 36px;
    left: 0; right: 0;
    text-align: center;
    font-size: 15px;
    letter-spacing: 9px;
    text-transform: uppercase;
  }

  /* Back */
  .card--back { background: var(--white); }
  .back-wave { position: absolute; inset: 0; }
  .back-brand {
    position: absolute;
    top: 34px; left: 40px;
    color: var(--navy);
  }
  .back-brand .brand-name { font-size: 40px; text-align: left; }
  .back-brand .brand-name span { display: block; }
  .back-brand .brand-name .brand-sub { font-size: 24px; letter-spacing: 7px; margin-top: 4px; }
  .company-info {
    margin-top: 12px;
    font-weight: 700;
    font-style: italic;
    font-size: 13px;
    line-height: 1.3;
    text-transform: uppercase;
    color: var(--navy);
  }
  .owner {
    position: absolute;
    top: 150px; right: 40px;
    text-align: right;
    font-family: "Oswald", sans-serif;
    text-transform: uppercase;
  }
  .owner-name { font-size: 24px; font-weight: 700; color: var(--navy); letter-spacing: .5px; }
  .owner-role { font-size: 16px; font-weight: 500; color: var(--accent-red); }
  .contacts {
    position: absolute;
    right: 36px; bottom: 26px;
    list-style: none;
    color: var(--white);
    font-size: 15px;
    text-align: right;
  }
  .contacts li { display: flex; align-items: center; justify-content: flex-end; gap: 10px; line-height: 1.65; }
  .contacts svg { width: 15px; height: 15px; fill: var(--accent-red); flex: none; }
</style>
</head>
<body>

<section class="card card--front" aria-label="Business card front">
  <h1 class="brand-name"><span>Harrowden</span><span class="brand-sub">Metal Recycling</span></h1>
  <p class="tagline">Recycling since 1950</p>
  <p class="front-web">www.harrowdenscrapworks.co.uk</p>
</section>

<section class="card card--back" aria-label="Business card back">
  <svg class="back-wave" viewBox="0 0 735 420" preserveAspectRatio="none" aria-hidden="true">
    <defs>
      <linearGradient id="silver" x1="0" y1="0" x2="1" y2="0">
        <stop offset="0" stop-color="var(--silver-dark)"/>
        <stop offset=".3" stop-color="var(--silver-light)"/>
        <stop offset=".6" stop-color="var(--silver-dark)"/>
        <stop offset="1" stop-color="var(--silver-light)"/>
      </linearGradient>
      <linearGradient id="panel" x1="0" y1="0" x2="1" y2="1">
        <stop offset="0" stop-color="var(--brand-blue)"/>
        <stop offset=".5" stop-color="var(--deep-blue)"/>
        <stop offset="1" stop-color="#2a3290"/>
      </linearGradient>
    </defs>
    <path d="M0 215 C 90 150, 200 200, 330 250 C 470 300, 620 250, 735 330 L 735 360 C 620 285, 470 330, 330 285 C 200 240, 90 205, 0 250 Z" fill="url(#silver)"/>
    <path d="M0 250 C 90 205, 200 240, 330 285 C 470 330, 620 285, 735 360 L 735 420 L 0 420 Z" fill="url(#panel)"/>
  </svg>

  <div class="back-brand">
    <h2 class="brand-name"><span>Harrowden</span><span class="brand-sub">Metal Recycling</span></h2>
    <p class="company-info">D.Harrowden Metals Ltd<br>Recycling scrap metals in<br>Croydon and South London<br>Since 1978</p>
  </div>

  <div class="owner">
    <p class="owner-name">Martin Harrowden</p>
    <p class="owner-role">Owner-Director</p>
  </div>

  <ul class="contacts">
    <li>079-555-014-82
      <svg viewBox="0 0 16 16" aria-hidden="true"><path d="M3 1h3l1.5 4-2 1.2a9 9 0 0 0 4.3 4.3L11 8.5l4 1.5v3a2 2 0 0 1-2 2A12 12 0 0 1 1 3a2 2 0 0 1 2-2z"/></svg></li>
    <li>020-555-306-47
      <svg viewBox="0 0 16 16" aria-hidden="true"><path d="M4 0h8a1 1 0 0 1 1 1v14a1 1 0 0 1-1 1H4a1 1 0 0 1-1-1V1a1 1 0 0 1 1-1zm1 2v10h6V2zm3 11a1 1 0 1 0 0 2 1 1 0 0 0 0-2z"/></svg></li>
    <li>info@harrowdenscrapworks.co.uk
      <svg viewBox="0 0 16 16" aria-hidden="true"><path d="M1 3h14v10H1zm1 1v.5l6 4 6-4V4zm0 2v6h12V6l-6 4z"/></svg></li>
    <li>harrowdenscrapworks.co.uk
      <svg viewBox="0 0 16 16" aria-hidden="true"><path d="M8 1a7 7 0 1 0 0 14A7 7 0 0 0 8 1zm0 1.3c.9.8 1.6 2.5 1.8 4.7H6.2C6.4 4.8 7.1 3.1 8 2.3zM2.3 8.7h2.6c.1 1.9.6 3.6 1.3 4.6a5.7 5.7 0 0 1-3.9-4.6zm0-1.4a5.7 5.7 0 0 1 3.9-4.6c-.7 1-1.2 2.7-1.3 4.6zm3.9 1.4h3.6c-.2 2.2-.9 3.9-1.8 4.7-.9-.8-1.6-2.5-1.8-4.7zm3.6 4.6c.7-1 1.2-2.7 1.3-4.6h2.6a5.7 5.7 0 0 1-3.9 4.6zm1.3-6c-.1-1.9-.6-3.6-1.3-4.6a5.7 5.7 0 0 1 3.9 4.6z"/></svg></li>
  </ul>
</section>

</body>
</html>
```